Personalised Poetry business needs a business card designed

I am a writer that specialises in personalised poetry for people for significant life events.
I want a business card that stands out and portrays class and professionalism but is also welcoming & indicates warmth and honesty.
I'm happy with the logo that was designed for me, I would like to see it in raised print on the business card. I am open to suggestions on colours but think perhaps gold or silver writing for the logo would look good. I would like just the logo and my name and contact details on the front of the card. On the back of the card, I would like a list of the different events I provide poems for I will upload a photo of my current business card for reference. My current logo has a shading behind it that I don't like, I just want the words of the logo without any background colour

Target Market(s)

People wanting to provide a unique gift to someone special in their life

Industry/Entity Type

Writer

Contact Information for Business Card

Logo, my name and contact details on the front and a list of all the events I write poetry for on the back

Font styles to use
Script

Requirements
Must have
• I would like to see the logo, if possible, in a raised type of print on the card so that you can feel the actual words. I would like to have a glossy finish to the card and be able to print it on good quality board
Should not have
• The shading that is currently behind the logo on my current business card

```html
<!DOCTYPE html>
<html lang="en">
<head>
<meta charset="utf-8">
<title>Lines for Always – Business Card</title>
<link href="https://fonts.googleapis.com/css2?family=Great+Vibes&family=Poppins:wght@300;400;600&display=swap" rel="stylesheet">
<style>
  :root{
    --backdrop:#232323;
    --card-dark:#1d1d1f;
    --paper:#ebeae8;
    --ink:#111112;
    --text-light:#f2f2f2;
    --text-muted:#a9a9ab;
    --emboss:#2a2a2d;
  }
  *{box-sizing:border-box;margin:0;padding:0}
  html,body{width:1200px;height:780px;overflow:hidden;background:var(--backdrop)}
  .sheet{position:relative;width:1200px;height:780px;display:flex;align-items:center;justify-content:center;gap:40px}
  .card{position:relative;width:540px;height:330px;border-radius:22px;background:var(--card-dark);overflow:hidden;box-shadow:0 18px 40px rgba(0,0,0,.55)}
  .card__art{position:absolute;inset:0;width:100%;height:100%}

  /* front */
  .brand{position:absolute;font-family:"Poppins",sans-serif;font-weight:400;color:var(--text-light)}
  .front .brand{left:230px;top:34px;font-size:24px;letter-spacing:.5px}
  .tagline{position:absolute;font-family:"Poppins",sans-serif;font-weight:300;font-size:11px;color:var(--text-muted);letter-spacing:.4px}
  .front .tagline{left:232px;top:68px}
  .identity{position:absolute;left:30px;top:108px;padding-left:14px;border-left:6px solid var(--text-light);font-family:"Poppins",sans-serif;color:var(--text-light)}
  .identity__name{font-size:25px;line-height:1.1;font-weight:300}
  .identity__name strong{font-weight:600}
  .identity__role{font-size:11px;font-weight:600;margin-top:3px}
  .contacts{position:absolute;left:30px;top:178px;list-style:none;font-family:"Poppins",sans-serif;font-weight:300;font-size:11.5px;color:var(--text-light)}
  .contacts li{display:flex;align-items:center;gap:9px;margin-bottom:6px}
  .contacts svg{width:12px;height:12px;flex:none}

  /* back */
  .back__heading{position:absolute;left:28px;top:24px;font-family:"Great Vibes",cursive;font-size:24px;color:var(--text-light)}
  .events{position:absolute;left:30px;top:70px;list-style:none;font-family:"Poppins",sans-serif;font-weight:300;font-size:12.5px;line-height:1.55;color:var(--text-light)}
  .events li{position:relative;padding-left:14px}
  .events li::before{content:"";position:absolute;left:0;top:8px;width:6px;height:6px;border-radius:50%;background:var(--text-light)}
  .back .brand{right:40px;top:128px;font-size:22px}
  .back .tagline{right:58px;top:160px}
</style>
</head>
<body>
<main class="sheet">

  <section class="card front" aria-label="Card front">
    <svg class="card__art" viewBox="0 0 540 330" role="img" aria-label="Line drawing of a hand writing with a fountain pen on a pale page">
      <defs>
        <linearGradient id="pageTone" x1="0" y1="0" x2="1" y2="1">
          <stop offset="0" stop-color="#efeeec"/>
          <stop offset="1" stop-color="#dddcda"/>
        </linearGradient>
      </defs>
      <path d="M210 330 C230 270 260 230 330 205 C400 180 450 150 540 120 L540 330 Z" fill="url(#pageTone)"/>
    </svg>
    <p class="brand">Lines for Always</p>
    <p class="tagline">Personalised Poetry</p>
    <div class="identity">
      <p class="identity__name"><strong>Marcus</strong> Ellery</p>
      <p class="identity__role">Writer &amp; Owner</p>
    </div>
    <ul class="contacts">
      <li><svg viewBox="0 0 12 12"><path d="M3 1 L5 3.5 L4 4.8 Q5.5 7 7.2 8 L8.5 7 L11 9 L9.8 11 Q4.5 10.5 1 3 Z" fill="#f2f2f2"/></svg>0400 555 017</li>
      <li><svg viewBox="0 0 12 12"><circle cx="6" cy="6" r="5" fill="none" stroke="#f2f2f2" stroke-width="1.2"/><path d="M1 6 H11 M6 1 Q3 6 6 11 Q9 6 6 1" fill="none" stroke="#f2f2f2" stroke-width="1"/></svg>www.linesforalways.com</li>
      <li><svg viewBox="0 0 12 12"><rect x="1" y="2.5" width="10" height="7" rx="1" fill="none" stroke="#f2f2f2" stroke-width="1.2"/><path d="M1.5 3 L6 6.5 L10.5 3" fill="none" stroke="#f2f2f2" stroke-width="1.1"/></svg>marcus@linesforalways.com</li>
    </ul>
  </section>

  <section class="card back" aria-label="Card back">
    <svg class="card__art" viewBox="0 0 540 330" role="img" aria-label="Raised tone-on-tone drawing of a hand holding a pen, with a looping line">
      <defs>
        <radialGradient id="embossTone" cx="0.65" cy="0.6" r="0.6">
          <stop offset="0" stop-color="#2b2b2e"/>
          <stop offset="1" stop-color="#1d1d1f"/>
        </radialGradient>
      </defs>
      <rect width="540" height="330" fill="url(#embossTone)"/>
    </svg>
    <p class="back__heading">Momentous Life Events Personalised in Poetry</p>
    <ul class="events">
      <li>Valentines Day</li>
      <li>Funerals &amp; Eulogies</li>
      <li>Birthdays &amp; Christmas</li>
      <li>Weddings &amp; Anniversaries</li>
      <li>Retirements, Business<br>&amp; Corporate Events</li>
    </ul>
    <p class="brand">Lines for Always</p>
    <p class="tagline">Personalised Poetry</p>
  </section>

</main>
</body>
</html>
```